"Orvana" - Ketamine Clinic - Save Minds and Heal Hearts!! -

I need a very nice modern happy brain themed warm website design for our cutting edge modern and caring ketamine IV infusion clinic that also offers talk therapy and telemedicine visits.
A great design using the color schemes in out logos (grey, white, purples and that need metallic fading colored effect in the logo).

```html
<!DOCTYPE html>
<html lang="en">
<head>
<meta charset="utf-8">
<title>Orvana – Ketamine Clinic</title>
<link href="https://fonts.googleapis.com/css2?family=Montserrat:wght@400;500;600;700&family=Oswald:wght@500;600&family=Kaushan+Script&display=swap" rel="stylesheet">
<style>
:root{
  --purple:#4a12c9;
  --violet:#7a1fd6;
  --cyan:#18b6f0;
  --ink:#1c1c24;
  --grey:#6b6b73;
  --text:#333339;
  --lav:#efe6fb;
  --line:#e6e2ee;
  --white:#fff;
  --black:#000;
  --btn:linear-gradient(90deg,#19b3f2 0%,#4b1ee0 55%,#3a0fb0 100%);
}
*{box-sizing:border-box;margin:0;padding:0}
html,body{width:1200px;height:4000px;overflow:hidden}
body{position:relative;background:var(--white);font-family:'Montserrat',sans-serif;color:var(--text)}
.abs{position:absolute}
.btn{position:absolute;display:flex;align-items:center;justify-content:center;background:var(--btn);color:#fff;font-size:12.5px;font-weight:500;height:39px;width:186px}
.section-title{position:absolute;left:0;width:1200px;text-align:center;font-size:37px;font-weight:500;color:var(--grey)}

/* hero */
.hero{left:0;top:0;width:1200px;height:600px;background:linear-gradient(100deg,#262a12 0%,#363d1c 35%,#5b6a3a 60%,#7f8f5a 80%,#4d5f2b 100%)}
.logo{position:absolute;display:flex;align-items:center;gap:10px;font-weight:700;font-size:34px}
.logo .dot{width:26px;height:26px;border-radius:50%;background:linear-gradient(135deg,#7b3fe4,#3b7de8)}
.hero-title{left:163px;top:212px;font-family:'Oswald',sans-serif;font-weight:500;font-size:41px;line-height:47px;color:#fff}
.hero-script{left:163px;top:318px;font-family:'Kaushan Script',cursive;font-size:25px;color:#fff}

.features{left:161px;top:543px;width:876px;height:119px;background:#fff;box-shadow:0 6px 20px rgba(0,0,0,.1);display:flex}
.feature{flex:1;display:flex;gap:16px;padding:26px 0 0 28px;border-right:1px solid var(--line)}
.feature:last-child{border:none}
.feature .ic{width:32px;height:32px;border-radius:50%;background:var(--lav);flex:none;margin-top:4px}
.feature h3{font-size:15px;font-weight:600;color:var(--ink);margin-bottom:6px}
.feature p{font-size:12px;line-height:23px}

/* about */
.about-img{left:0;top:753px;width:483px;height:441px;background:linear-gradient(120deg,#e8e6e2,#b9b3a8 50%,#5a4a6e)}
.about-text{left:543px;top:750px;width:490px}
.about-text h2{font-size:36px;font-weight:500;color:var(--grey);margin-bottom:12px}
.about-text p{font-size:12px;line-height:23px;margin-bottom:6px}

/* services */
.services-intro{left:200px;top:1330px;width:800px;text-align:center;font-size:12px;line-height:23px}
.service{position:absolute;display:flex;align-items:center;gap:20px;width:420px}
.service .ring{width:87px;height:87px;border-radius:50%;border:2.5px solid var(--violet);display:flex;align-items:center;justify-content:center;flex:none}
.service .ring span{width:50px;height:50px;border-radius:50%;background:linear-gradient(135deg,#dcd0fa,#bde6fb)}
.service h3{font-size:15px;font-weight:600;color:var(--ink);margin-bottom:6px}
.service p{font-size:12px;line-height:23px}

/* banner */
.banner{left:0;top:1887px;width:1200px;height:112px;background:linear-gradient(90deg,#17b6ee 0%,#6b21e0 40%,#8a1ee0 70%,#5b10c8 100%)}
.banner .circ{position:absolute;left:161px;top:17px;width:78px;height:78px;border-radius:50%;border:2px solid #fff;display:flex;align-items:center;justify-content:center}
.banner h2{position:absolute;left:266px;top:38px;font-size:26px;font-weight:500;color:#fff}
.banner .light{position:absolute;left:851px;top:36px;width:187px;height:40px;background:#fff;color:var(--ink);font-size:12.5px;font-weight:500;display:flex;align-items:center;justify-content:center}

/* testimonials */
.testi{left:0;top:1999px;width:1200px;height:598px;background:linear-gradient(160deg,#e5e3fa 0%,#f3eefc 50%,#f0e3fb 100%)}
.card{position:absolute;top:2207px;width:277px;height:276px;background:#fff}
.card .date{position:absolute;left:22px;top:22px;font-size:12px}
.card .quote{position:absolute;left:22px;top:52px;width:240px;font-size:13px;line-height:25.5px}
.card .stars{position:absolute;left:22px;top:160px;color:#f79a2a;font-size:16px;letter-spacing:1px}
.card .qm{position:absolute;right:20px;top:140px;font-size:96px;line-height:1;color:#d9cdf6;font-weight:700}
.card .foot{position:absolute;left:0;top:212px;width:100%;height:64px;border-top:1px solid var(--line);display:flex;align-items:center;gap:12px;padding-left:22px}
.card .av{width:38px;height:38px;border-radius:50%;background:linear-gradient(135deg,#d9cfc5,#8a7b70)}
.card .nm{font-size:14px;font-weight:600;color:var(--ink)}
.card .rl{font-size:11px;color:#999}

/* story */
.story-title{left:161px;top:2752px;width:520px;font-size:36px;line-height:47px;font-weight:500;color:var(--grey)}
.story-copy{left:161px;top:2912px;width:500px;font-size:13px;line-height:25px}
.story-img{left:716px;top:2687px;width:484px;height:441px;background:linear-gradient(110deg,#f1eee9 0%,#d8cfc3 45%,#7a6a60 75%,#3e4a66 100%)}

/* form */
.footer{left:0;top:3487px;width:1200px;height:513px;background:var(--black)}
.panel{left:236px;top:3487px;width:727px;height:144px;background:#fff}
.field{position:absolute;border:1px solid #cfcfd6;font-size:10.5px;color:#777;padding:13px 14px}
.submit{left:536px;top:3535px;width:127px;height:40px;font-size:12px}
.flogo{left:0;top:3680px;width:1200px;justify-content:center;color:#b7a8d8}
.contact{position:absolute;top:3856px;display:flex;align-items:center;gap:18px;color:#fff;font-size:13px;line-height:20px}
.contact .c{width:44px;height:44px;border-radius:50%;background:#fff;display:flex;align-items:center;justify-content:center}
.copy{left:161px;top:3955px;font-size:12px;color:#fff}
.social{left:898px;top:3951px;display:flex;gap:8px}
.social span{width:29px;height:29px;border:1px solid #fff}
</style>
</head>
<body>

<section class="abs hero" role="img" aria-label="Smiling woman blowing soap bubbles outdoors in a green park"></section>
<div class="logo" style="left:163px;top:40px;color:#fff"><span class="dot"></span>Orvana</div>
<div class="btn" style="left:851px;top:47px">Request a Consultation</div>
<h1 class="abs hero-title">The Premier Ketamine<br>Treatment Provider</h1>
<p class="abs hero-script">Redefining The Meaning of Happiness</p>
<div class="btn" style="left:161px;top:370px">Request a Consultation</div>

<div class="abs features">
  <div class="feature"><span class="ic"></span><div><h3>Affordable for Anyone</h3><p>Lorem ipsum dolor sit amettur<br>adipiscing elit quis quam.</p></div></div>
  <div class="feature"><span class="ic"></span><div><h3>Doctor Prescribed</h3><p>Lorem ipsum dolor sit amettur<br>adipiscing elit quis quam.</p></div></div>
  <div class="feature"><span class="ic"></span><div><h3>Support Staff</h3><p>Lorem ipsum dolor sit amettur<br>adipiscing elit quis quam.</p></div></div>
</div>

<div class="abs about-img" role="img" aria-label="Therapist taking notes during a talk session with a patient"></div>
<div class="abs about-text">
  <h2>About Orvana.com</h2>
  <p>Lorem ipsum dolor sit amet, consectetur adipiscing elit. Quisque quis quammu pellentesque dui in varius odio. Nunc convallis bibendum semorttitor tincidunt. Vivamus id massa in lectus fringilla interdum et non nisi. Vestibulum id felislisis sollicitudin ante non, placerat lectus.</p>
  <p>Mauris non augue mattist metus a feugiat purus. Phasellus eu puruslesuada, feugiat nisl non blandit enim. Morbi ante massa, tincidunt ac aliquet elerisque at eros. Maecenas a diam a urna aliquet vehicula quis ac neque.</p>
  <p>Lorem ipsum dolor sit amet, consectetur adipiscing elit. Quisque quis quammu pellentesque dui in varius odio. Nunc convallis bibendum semorttitor tincidunt. Vivamus id massa in lectus fringilla interdum et non nisi. Vestibulum id felislisis sollicitudin ante non, placerat lectus.</p>
  <p>Mauris non augue mattist metus a feugiat purus. Phasellus eu puruslesuada, feugiat nisl non blandit enim. Morbi ante massa, tincidunt ac aliquet elerisque at eros. Maecenas a diam a urna aliquet vehicula quis ac neque.</p>
</div>
<div class="btn" style="left:543px;top:1152px">Request a Consultation</div>

<h2 class="section-title" style="top:1276px">Our Services</h2>
<p class="abs services-intro">Lorem ipsum dolor sit amet consectetur adipiscing elit. Quisque quis quammu pellentesque dui in varius odio. Nunc convallis bibendum semorttitor tincidunt massa in lectus fringilla interdum et non nisi. Vestibulum id felislisis sollicitudin.</p>
<div class="service" style="left:161px;top:1402px"><span class="ring"><span></span></span><div><h3>Depression</h3><p>Lorem ipsum dolor sit amet conse etadipiscing elit.<br>Quisque quis quam aliquam...</p></div></div>
<div class="service" style="left:632px;top:1402px"><span class="ring"><span></span></span><div><h3>Anxiety</h3><p>Lorem ipsum dolor sit amet conse etadipiscing<br>elit. Quisque quis quam aliquam...</p></div></div>
<div class="service" style="left:161px;top:1520px"><span class="ring"><span></span></span><div><h3>PTSD</h3><p>Lorem ipsum dolor sit amet conse etadipiscing elit.<br>Quisque quis quam aliquam...</p></div></div>
<div class="service" style="left:632px;top:1520px"><span class="ring"><span></span></span><div><h3>Bipolar Disorder</h3><p>Lorem ipsum dolor sit amet conse etadipiscing<br>elit. Quisque quis quam aliquam...</p></div></div>
<div class="service" style="left:161px;top:1638px"><span class="ring"><span></span></span><div><h3>Migraines</h3><p>Lorem ipsum dolor sit amet conse etadipiscing elit.<br>Quisque quis quam aliquam...</p></div></div>
<div class="service" style="left:632px;top:1638px"><span class="ring"><span></span></span><div><h3>Chronic Pain</h3><p>Lorem ipsum dolor sit amet conse etadipiscing<br>elit. Quisque quis quam aliquam...</p></div></div>
<div class="btn" style="left:507px;top:1756px">Request a Consultation</div>

<section class="abs banner">
  <div class="circ"><svg width="40" height="40" viewBox="0 0 40 40" fill="none" stroke="#fff" stroke-width="2"><rect x="5" y="8" width="30" height="26" rx="3"/><line x1="5" y1="15" x2="35" y2="15"/><line x1="12" y1="4" x2="12" y2="11"/><line x1="28" y1="4" x2="28" y2="11"/><path d="M14 24l4 4 8-8"/></svg></div>
  <h2>Schedule For Ketamine IV Infusion Therapy</h2>
  <div class="light">Request a Consultation</div>
</section>

<section class="abs testi"></section>
<h2 class="section-title" style="top:2128px">What Patients Are Saying..</h2>
<div class="card" style="left:161px"><span class="date">09th October 2023</span><p class="quote">Lorem ipsum dolor sit consectetur adipiscing elit. Quisque quis quam aliquam, pellentesque dui in varius odio. Nunc convallis bibendum...</p><span class="stars">★★★★★</span><span class="qm">”</span><div class="foot"><span class="av"></span><div><div class="nm">Ethan Rowley</div><div class="rl">Patient</div></div></div></div>
<div class="card" style="left:461px"><span class="date">09th October 2023</span><p class="quote">Lorem ipsum dolor sit consectetur adipiscing elit. Quisque quis quam aliquam, pellentesque dui in varius odio. Nunc convallis bibendum...</p><span class="stars">★★★★★</span><span class="qm">”</span><div class="foot"><span class="av"></span><div><div class="nm">Clara Benning</div><div class="rl">Patient</div></div></div></div>
<div class="card" style="left:761px"><span class="date">09th October 2023</span><p class="quote">Lorem ipsum dolor sit consectetur adipiscing elit. Quisque quis quam aliquam, pellentesque dui in varius odio. Nunc convallis bibendum...</p><span class="stars">★★★★★</span><span class="qm">”</span><div class="foot"><span class="av"></span><div><div class="nm">Owen Hale</div><div class="rl">Patient</div></div></div></div>

<h2 class="abs story-title">Lorem Ipsum Dlor Sit Amet Consectetur Adipiscing Elit. Quisque Quis Qua.</h2>
<p class="abs story-copy">Pellentesque Et Risus Nec Sem Euismod Elementum Ornare Vel Velit. Sed Euismod Enim Dolor, Nec Molestie Nunc Vestibulum Vitae. Aen Vestibulum Dolor In Eleifend Ultrices. Fusce Porttitor Scelerisque Fringilla.</p>
<div class="btn" style="left:161px;top:3010px">Request a Consultation</div>
<div class="abs story-img" role="img" aria-label="Happy couple embracing at home by a bright window"></div>

<section class="abs footer"></section>
<div class="abs panel"></div>
<h2 class="section-title" style="top:3210px">Request a Consultation</h2>
<div class="field" style="left:284px;top:3283px;width:308px;height:42px">Name*</div>
<div class="field" style="left:607px;top:3283px;width:308px;height:42px">Phone*</div>
<div class="field" style="left:284px;top:3342px;width:308px;height:42px">Email*</div>
<div class="field" style="left:607px;top:3342px;width:308px;height:42px">Inquiry For*
  <svg style="position:absolute;right:12px;top:15px" width="14" height="10" viewBox="0 0 14 10" fill="none" stroke="#444" stroke-width="1.5"><path d="M1 2l6 6 6-6"/></svg></div>
<div class="field" style="left:284px;top:3401px;width:631px;height:106px;background:#fff">Message</div>
<div class="btn submit">Submit Now</div>

<div class="logo abs flogo"><span class="dot"></span>Orvana</div>
<div class="contact" style="left:253px"><span class="c"><svg width="20" height="20" viewBox="0 0 24 24" fill="#4a12c9"><path d="M6.6 10.8a15 15 0 006.6 6.6l2.2-2.2c.3-.3.7-.4 1-.2 1.1.4 2.3.6 3.6.6.6 0 1 .4 1 1V20c0 .6-.4 1-1 1A17 17 0 013 4c0-.6.4-1 1-1h3.5c.6 0 1 .4 1 1 0 1.3.2 2.5.6 3.6.1.3 0 .7-.2 1z"/></svg></span><div>Phone No<br>123 456 7890</div></div>
<div class="contact" style="left:478px"><span class="c"><svg width="20" height="20" viewBox="0 0 24 24" fill="#4a12c9"><path d="M12 2a7 7 0 00-7 7c0 5 7 13 7 13s7-8 7-13a7 7 0 00-7-7zm0 9.5A2.5 2.5 0 1112 6a2.5 2.5 0 010 5.5z"/></svg></span><div>123 Ut Wisi Enim Ad Minim<br>Veniam Quis Nostrud.</div></div>
<div class="contact" style="left:779px"><span class="c"><svg width="20" height="20" viewBox="0 0 24 24" fill="none" stroke="#4a12c9" stroke-width="2"><rect x="3" y="5" width="18" height="14" rx="2"/><path d="M3 7l9 6 9-6"/></svg></span><div>Email<br>info@orvana.com</div></div>
<p class="abs copy">Copyright © 2023 Orvana.com. All Rights Reserved.</p>
<div class="abs social"><span></span><span></span><span></span><span></span></div>

</body>
</html>
```